Creative Brief
Eastmoor Directorate - Bahrain
Business Cards + Stationary materials.
Simple
Tariq Yousef Al-Mansoori
Head of Financial Affairs
P.O. Box 37182, Awali. Kingdom of Bahrain
talmansoori@eastmoor-dir.example
www.eastmoor-dir.example
We would like the design to include the following colors : cyan, golden & silver. But we are open to new ideas that match our new logo.
Stationary items include :
- A4 letterhead ( would prefer the logo in the top middle section so that we can write the office name on either side of the A4 paper. We would like to use the attached watermark image ( you can change the color to match the theme )
- Notepad
- Presentation folder
- Envelopes ( A4, A3, basically the whole nine yards)
a short explanation on the attached files :
* ED Logo : main logo that represents our office (available in B&W and colored)
* Watermark : design we want as a watermark on the stationary
* Horizon : logo (available in different sizes) that should appear close to the address line and should appear on all stationary materials and business cards. This represents Bahrain horizon plan for economic development, more info can be found here : http://www.horizonplan.example/web/ , or http://wiki.example.org/wiki/Bahrain_Horizon_Plan
We would like to also point out that the back side of the business card MUST include the same information as the front but in Arabic language, you can find the translated info below.
Name : طارق يوسف المنصوري
Title : رئيس الموارد المالية
address :
ص.ب 37182، عوالي. مملكة البحرين
all the other info should be the same.
We wouldn't mind seeing different types of fonts as long as they are professional, serious and formal.
ED Logo : main logo that represents our office - in black and white
ED Logo : main logo that represents our office - colored
design we want as a watermark on the stationary
logo that should appear close to the address line and should appear on all stationary materials and business cards. This represents Bahrain horizon plan for economic development, more info can be found here : http://www.horizonplan.example/web/ ,or http://wiki.example.org/wiki/Bahrain_Horizon_Plan

```html
<!DOCTYPE html>
<html lang="en">
<head>
<meta charset="utf-8">
<title>Eastmoor Directorate – Stationery</title>
<link rel="stylesheet" href="https://fonts.googleapis.com/css2?family=Open+Sans:wght@400;600;700&family=Noto+Naskh+Arabic:wght@400;700&display=swap">
<style>
  :root{
    --stage:#e9e6e1;
    --gold-light:#e6c890;
    --gold:#d4ad6c;
    --gold-dark:#b98f4e;
    --blue:#1c5ea6;
    --blue-soft:#4d7fb8;
    --red:#c8202a;
    --paper:#ffffff;
    --mark-faint:rgba(255,255,255,.35);
    --mark-grey:rgba(120,120,120,.12);
  }
  *{margin:0;padding:0;box-sizing:border-box}
  html,body{width:1200px;height:794px;overflow:hidden}
  body{background:var(--stage);font-family:"Open Sans",Arial,sans-serif;position:relative;color:var(--blue)}
  .piece{position:absolute;box-shadow:0 2px 8px rgba(0,0,0,.25)}
  .gold{background:linear-gradient(135deg,var(--gold-light),var(--gold) 55%,var(--gold-dark))}
  .arabic{font-family:"Noto Naskh Arabic",serif;direction:rtl}
  .badge{position:absolute;display:flex;align-items:center;gap:5px;font-weight:700;color:var(--blue);white-space:nowrap}
  .badge .dot{width:14px;height:14px;border-radius:50%;background:var(--blue);flex:none}
  .horizon{position:absolute;display:flex;align-items:center;gap:4px;font-weight:700;color:var(--red);font-size:9px}
  .horizon .sq{width:8px;height:8px;background:var(--red)}
  .watermark{position:absolute;border-radius:40%;background:radial-gradient(ellipse,var(--mark-faint),transparent 70%)}
  .watermark.on-white{background:radial-gradient(ellipse,var(--mark-grey),transparent 70%)}
  .small{font-size:7.5px;line-height:1.45;color:var(--blue)}

  /* business card – Arabic back */
  .card-back{left:12px;top:12px;width:336px;height:185px}
  .card-back .name{position:absolute;right:14px;top:10px;font-size:13px;font-weight:700;line-height:1.2;text-align:right}
  .card-back .contact{position:absolute;left:16px;top:112px;direction:ltr}

  /* business card – English front */
  .card-front{left:290px;top:212px;width:330px;height:185px}
  .card-front .name{position:absolute;right:14px;top:14px;text-align:right}
  .card-front .name strong{display:block;font-size:12px;font-weight:600}
  .card-front .name span{font-size:9px}
  .card-front .contact{position:absolute;left:16px;top:95px}

  /* DL envelope flap */
  .env-dl{left:12px;top:412px;width:588px;height:115px}

  /* A4 envelope */
  .env-a4{left:50px;top:540px;width:550px;height:200px}
  .env-a4 .addr{position:absolute;left:20px;top:12px;font-size:14px;font-weight:600;line-height:1.25}

  /* letterhead */
  .letterhead{left:640px;top:12px;width:548px;height:770px;background:var(--paper)}
  .letterhead .footer-addr{position:absolute;right:18px;bottom:26px;font-size:13px;font-weight:600}
  .letterhead .footer-contact{position:absolute;right:18px;bottom:10px;font-size:7.5px;display:flex;gap:20px}
</style>
</head>
<body>

  <section class="piece gold card-back" aria-label="Business card, Arabic side">
    <div class="name arabic">طارق يوسف المنصوري<br><span style="font-size:11px;font-weight:400">رئيس الموارد المالية</span></div>
    <div class="watermark" role="img" aria-label="Faint Arabic calligraphy watermark" style="left:110px;top:50px;width:110px;height:60px"></div>
    <div class="contact small">
      <div class="arabic" style="direction:rtl;text-align:left">ص.ب 37182، عوالي. مملكة البحرين</div>
      T: (973) 1700 0101<br>M: (973) 3600 0202<br>F: (973) 1700 0303<br>
      talmansoori@eastmoor-dir.example<br>www.eastmoor-dir.example
    </div>
    <div class="badge" style="left:200px;top:128px;font-size:9px"><span class="dot"></span>Eastmoor Directorate</div>
    <div class="horizon" style="left:16px;top:8px"><span class="sq"></span>Horizon</div>
  </section>

  <section class="piece gold card-front" aria-label="Business card, English side">
    <div class="name"><strong>Tariq Yousef Al-Mansoori</strong><span>Head of Financial Affairs</span></div>
    <div class="horizon" style="left:16px;top:16px"><span class="sq"></span>Horizon</div>
    <div class="watermark" role="img" aria-label="Faint Arabic calligraphy watermark" style="left:120px;top:70px;width:110px;height:60px"></div>
    <div class="contact small">
      P.O. Box 37182, Awali<br>Kingdom of Bahrain<br>
      T: (973) 1700 0101<br>M: (973) 3600 0202<br>F: (973) 1700 0303<br>
      talmansoori@eastmoor-dir.example<br>www.eastmoor-dir.example
    </div>
    <div class="badge" style="left:196px;top:135px;font-size:9px"><span class="dot"></span>Eastmoor Directorate</div>
  </section>

  <section class="piece gold env-dl" aria-label="DL envelope, flap">
    <svg width="588" height="115" viewBox="0 0 588 115" style="position:absolute;inset:0">
      <path d="M0 0 H588 V40 Q294 120 0 40 Z" fill="rgba(255,255,255,.18)" stroke="rgba(150,110,50,.5)"/>
    </svg>
    <div class="watermark" role="img" aria-label="Faint Arabic calligraphy watermark" style="left:40px;top:25px;width:90px;height:45px"></div>
    <div class="watermark" role="img" aria-label="Faint Arabic calligraphy watermark" style="right:40px;top:25px;width:90px;height:45px"></div>
    <div class="badge" style="left:210px;top:42px;font-size:11px"><span class="dot"></span>Eastmoor Directorate</div>
  </section>

  <section class="piece gold env-a4" aria-label="A4 envelope">
    <div class="addr">P.O. Box 37182, Awali.<br>Kingdom of Bahrain</div>
    <div class="badge" style="right:18px;top:18px;font-size:10px"><span class="dot"></span>Eastmoor Directorate</div>
    <div class="watermark" role="img" aria-label="Faint Arabic calligraphy watermark" style="left:200px;top:80px;width:150px;height:80px"></div>
    <div class="horizon" style="left:20px;bottom:14px"><span class="sq"></span>Horizon</div>
  </section>

  <section class="piece letterhead" aria-label="A4 letterhead">
    <div class="badge" style="right:22px;top:28px;font-size:12px"><span class="dot"></span>Eastmoor Directorate</div>
    <div class="watermark on-white" role="img" aria-label="Faint Arabic calligraphy watermark" style="left:110px;top:300px;width:330px;height:180px"></div>
    <div class="horizon" style="left:18px;bottom:26px"><span class="sq"></span>Horizon</div>
    <div class="footer-addr">P.O. Box 37182, Awali. Kingdom of Bahrain</div>
    <div class="footer-contact">
      <span>T: (973) 1700 0101</span><span>C: (973) 3600 0202</span><span>F: (973) 1700 0303</span>
      <span>E: talmansoori@eastmoor-dir.example</span><span>www.eastmoor-dir.example</span>
    </div>
  </section>

</body>
</html>
```